WINE LABEL for Cobble-K Estate.

We require a wine bottle label for our Cobble-K Estate brand new to the market.
A sample "mock-up" layout of the front and back label is attached. The Cobble-K writing can be a logo type design with any font the designer chooses keeping in mind this will be used on Stationary, business cards and vehicles as well so could included some creative design as long as its clear to read the "Cobble-K" We require a pair of "crusty cowboy boots" as the main theme of the label but the designer could use flair here and design inside a circle or leave as set out.The main thing is they are rugged looking. The label can be framed if appropriate and the use of a parchment look or old western looking idea could be used. We would limit colors to 3 for printing purposes so the combination of colors is up to the designer as long as it stands out on the label visually. The rear label components is attached but can be set-out in any form the designer chooses. The use of the mountain outline at the base of the rear label may add a nice addition to this as its the view we see from our vineyard. Anything else please message me directly.

Target Market(s)

Boutique vineyard label that stands out from the normal.

Contact Information for Business Card

Set out using the designs from the label.

Font styles to use
Other font styles liked:
• Designer to use their selection

Requirements
Must have
• as set out on attached label Mock-up.
• A western theme for the label is preferred.
Should not have
• photos or more than 3 colours

```html
<!DOCTYPE html>
<html lang="en">
<head>
<meta charset="utf-8">
<title>Cobble-K Estate – Wine Label Presentation</title>
<link rel="stylesheet" href="https://fonts.googleapis.com/css2?family=Old+Standard+TT:ital,wght@0,400;0,700;1,400&family=Roboto+Condensed:ital,wght@1,300;1,400&display=swap">
<style>
  :root{
    --board:#231210;
    --note:#d9a878;
    --cream:#f2e7d5;
    --parchment:#ebdcc2;
    --ink:#141010;
    --brown:#9a6644;
    --brown-dark:#6e4429;
    --swatch-frame:#cdb99c;
  }
  *{box-sizing:border-box;margin:0;padding:0}
  html,body{width:1200px;height:1000px;overflow:hidden;background:var(--board)}
  .board{position:relative;width:1200px;height:1000px;background:var(--board);font-family:"Roboto Condensed",Arial,sans-serif;color:var(--note)}
  .board-title{position:absolute;left:24px;top:20px;font-style:italic;font-size:21px;font-weight:400;color:var(--note)}

  .note{position:absolute;left:693px;width:440px;text-align:center;font-style:italic;font-weight:300;font-size:13.5px;line-height:19px;color:var(--note);letter-spacing:.2px}
  .note--intro{top:86px}
  .note--intro p+p{margin-top:11px}
  .note--emboss{top:492px}

  /* front label, sized in em so it scales */
  .front-label{position:absolute;width:20em;height:25em;font-family:"Old Standard TT",Georgia,serif;color:var(--ink)}
  .front-label--hero{left:227px;top:288px;font-size:17px}
  .front-label--pair-a{left:753px;top:555px;font-size:8.25px}
  .front-label--pair-b{left:922px;top:555px;font-size:8.25px}
  .label-frame{position:absolute;inset:0;width:100%;height:100%}
  .front-label .brand{position:absolute;top:1.35em;left:0;right:0;text-align:center;font-size:1.85em;font-weight:700;color:var(--brown);letter-spacing:.02em;white-space:nowrap}
  .emblem{position:absolute;top:4.7em;left:4.3em;width:11.4em;height:10.6em;border-radius:50%;border:.08em solid var(--brown-dark);background:radial-gradient(ellipse at 50% 45%,#e9dcc5 0%,#cdb796 70%,#b89c78 100%)}
  .est{position:absolute;font-size:.95em;line-height:1;color:var(--ink)}
  .est--word{left:6.2em;top:11.9em}
  .est--year{right:5.6em;top:11.3em}
  .ribbon{position:absolute;top:15.3em;left:1.4em;width:17.2em;height:3em}
  .ribbon-text{position:absolute;top:15.75em;left:0;right:0;text-align:center;color:var(--cream);line-height:1;white-space:nowrap}
  .ribbon-text .region{display:block;font-size:.9em;letter-spacing:.04em}
  .ribbon-text .subregion{display:block;font-size:.5em;letter-spacing:.12em;margin-top:.2em}
  .varietal{position:absolute;top:18.9em;left:0;right:0;text-align:center;line-height:1.15;white-space:nowrap}
  .varietal .small{display:block;font-size:.72em;color:var(--ink)}
  .varietal .grape{display:block;font-size:1.25em;color:var(--ink)}
  .vintage{position:absolute;top:22.15em;left:4em;right:4em;display:flex;align-items:center;gap:.4em}
  .vintage .rule{flex:1;height:.07em;background:var(--brown)}
  .vintage .year{background:var(--brown);color:var(--cream);font-size:.85em;padding:.05em .9em;border-radius:1em}

  /* back label */
  .back-label{position:absolute;left:818px;top:212px;width:190px;height:238px;font-family:"Old Standard TT",Georgia,serif;color:var(--ink)}
  .back-label .brand{position:absolute;top:14px;left:0;right:0;text-align:center;font-size:16px;font-weight:700;color:var(--brown)}
  .back-copy{position:absolute;top:42px;left:14px;right:14px;text-align:center;font-size:9.5px;line-height:12.5px}
  .back-copy .producer{font-weight:700;font-size:10.5px}
  .back-copy .web{font-weight:700;margin-top:3px;display:block}
  .back-meta{position:absolute;top:146px;left:16px;right:16px;display:flex;align-items:flex-start;gap:6px}
  .badge{width:14px;height:14px;background:var(--ink);flex:none}
  .badge--outline{background:none;border:1.2px solid var(--ink)}
  .back-meta .fine{font-size:5.5px;line-height:7px;flex:1}
  .back-meta .abv{display:block;font-size:6.5px;margin-bottom:2px}
  .mountains{position:absolute;left:10px;right:10px;bottom:10px;height:42px;background:linear-gradient(180deg,var(--parchment) 0%,#b9a587 55%,#6f5e4b 100%)}

  /* specs */
  .spec{position:absolute;font-style:italic;font-weight:300;font-size:13.5px;color:var(--note)}
  .spec--size{left:695px;top:842px}
  .spec--color{left:691px;top:875px}
  .palette{position:absolute;left:734px;top:870px;width:132px;height:43px;background:var(--swatch-frame);display:flex;gap:6px;padding:6px 6px}
  .palette .chip{flex:1}
  .chip--cream{background:var(--cream)}
  .chip--black{background:var(--ink)}
  .chip--brown{background:var(--brown)}
</style>
</head>
<body>
<main class="board">
  <h1 class="board-title">Mockup</h1>

  <!-- front label, large -->
  <article class="front-label front-label--hero">
    <svg class="label-frame" viewBox="0 0 200 250" preserveAspectRatio="none" aria-hidden="true">
      <path d="M12,0 H188 A12 12 0 0 0 200 12 V238 A12 12 0 0 0 188 250 H12 A12 12 0 0 0 0 238 V12 A12 12 0 0 0 12 0Z" fill="var(--cream)" stroke="var(--brown-dark)" stroke-width="1"/>
      <path d="M16,5 H184 A11 11 0 0 0 195 16 V234 A11 11 0 0 0 184 245 H16 A11 11 0 0 0 5 234 V16 A11 11 0 0 0 16 5Z" fill="none" stroke="var(--ink)" stroke-width=".6"/>
    </svg>
    <div class="brand">Cobble-K Estate</div>
    <div class="emblem" role="img" aria-label="Pencil drawing of a pair of crusty cowboy boots with a grape vine leaf inside an oval"></div>
    <span class="est est--word">Est</span>
    <span class="est est--year">2009</span>
    <svg class="ribbon" viewBox="0 0 172 30" preserveAspectRatio="none" aria-hidden="true">
      <path d="M0,8 H22 V26 H0 L7,17Z" fill="var(--ink)"/>
      <path d="M172,8 H150 V26 H172 L165,17Z" fill="var(--ink)"/>
      <path d="M16,2 Q86,-2 156,2 V22 Q86,18 16,22Z" fill="var(--ink)"/>
    </svg>
    <div class="ribbon-text"><span class="region">STONEBRIDGE VALLEY</span><span class="subregion">HIGH PLAINS</span></div>
    <div class="varietal">
      <span class="small">Single Vineyard</span>
      <span class="grape">Grenache</span>
      <span class="small">Estate Grown Wine</span>
    </div>
    <div class="vintage"><span class="rule"></span><span class="year">2018</span><span class="rule"></span></div>
  </article>

  <div class="note note--intro">
    <p>The penicl drawing styles are combined with elegant Serifs Fonts,</p>
    <p>which bings the vintage, proffessional, premiumn and western feeling.</p>
    <p>The bright color stands out from the wine bottle.<br>It is easy for customer to regconize</p>
  </div>

  <!-- back label -->
  <article class="back-label">
    <svg class="label-frame" viewBox="0 0 190 238" preserveAspectRatio="none" aria-hidden="true">
      <path d="M11,0 H179 A11 11 0 0 0 190 11 V227 A11 11 0 0 0 179 238 H11 A11 11 0 0 0 0 227 V11 A11 11 0 0 0 11 0Z" fill="var(--cream)" stroke="var(--brown-dark)" stroke-width="1"/>
      <path d="M15,5 H175 A10 10 0 0 0 185 15 V223 A10 10 0 0 0 175 233 H15 A10 10 0 0 0 5 223 V15 A10 10 0 0 0 15 5Z" fill="none" stroke="var(--ink)" stroke-width=".6"/>
    </svg>
    <div class="brand">Cobble-K Estate</div>
    <div class="back-copy">
      <div class="producer">Produced &amp; Bottled By:</div>
      Cobble-K Estate Ltd<br>
      418 Stonebridge Rd<br>
      R D 3 Ashford 7712<br>
      High Plains NZ
      <span class="web">www.cobblekestate.co.nz</span>
    </div>
    <div class="back-meta">
      <span class="badge"></span>
      <span class="badge badge--outline"></span>
      <span class="fine"><span class="abv">13% vol. &nbsp;750ml</span>Contains Sulphites. Fined with egg products and traces may remain</span>
    </div>
    <div class="mountains" role="img" aria-label="Pencil drawing of the mountain range seen from the vineyard"></div>
  </article>

  <p class="note note--emboss">The logo should be embossed printing</p>

  <!-- front label pair -->
  <article class="front-label front-label--pair-a">
    <svg class="label-frame" viewBox="0 0 200 250" preserveAspectRatio="none" aria-hidden="true">
      <path d="M12,0 H188 A12 12 0 0 0 200 12 V238 A12 12 0 0 0 188 250 H12 A12 12 0 0 0 0 238 V12 A12 12 0 0 0 12 0Z" fill="var(--cream)" stroke="var(--brown-dark)" stroke-width="1"/>
      <path d="M16,5 H184 A11 11 0 0 0 195 16 V234 A11 11 0 0 0 184 245 H16 A11 11 0 0 0 5 234 V16 A11 11 0 0 0 16 5Z" fill="none" stroke="var(--ink)" stroke-width=".6"/>
    </svg>
    <div class="brand">Cobble-K Estate</div>
    <div class="emblem" role="img" aria-label="Pencil drawing of a pair of crusty cowboy boots with a grape vine leaf inside an oval"></div>
    <span class="est est--word">Est</span>
    <span class="est est--year">2009</span>
    <svg class="ribbon" viewBox="0 0 172 30" preserveAspectRatio="none" aria-hidden="true">
      <path d="M0,8 H22 V26 H0 L7,17Z" fill="var(--ink)"/>
      <path d="M172,8 H150 V26 H172 L165,17Z" fill="var(--ink)"/>
      <path d="M16,2 Q86,-2 156,2 V22 Q86,18 16,22Z" fill="var(--ink)"/>
    </svg>
    <div class="ribbon-text"><span class="region">STONEBRIDGE VALLEY</span><span class="subregion">HIGH PLAINS</span></div>
    <div class="varietal">
      <span class="small">Single Vineyard</span>
      <span class="grape">Grenache</span>
      <span class="small">Estate Grown Wine</span>
    </div>
    <div class="vintage"><span class="rule"></span><span class="year">2018</span><span class="rule"></span></div>
  </article>

  <article class="front-label front-label--pair-b">
    <svg class="label-frame" viewBox="0 0 200 250" preserveAspectRatio="none" aria-hidden="true">
      <path d="M12,0 H188 A12 12 0 0 0 200 12 V238 A12 12 0 0 0 188 250 H12 A12 12 0 0 0 0 238 V12 A12 12 0 0 0 12 0Z" fill="var(--cream)" stroke="var(--brown-dark)" stroke-width="1"/>
      <path d="M16,5 H184 A11 11 0 0 0 195 16 V234 A11 11 0 0 0 184 245 H16 A11 11 0 0 0 5 234 V16 A11 11 0 0 0 16 5Z" fill="none" stroke="var(--ink)" stroke-width=".6"/>
    </svg>
    <div class="brand">Cobble-K Estate</div>
    <div class="emblem" role="img" aria-label="Pencil drawing of a pair of crusty cowboy boots with a grape vine leaf inside an oval"></div>
    <span class="est est--word">Est</span>
    <span class="est est--year">2009</span>
    <svg class="ribbon" viewBox="0 0 172 30" preserveAspectRatio="none" aria-hidden="true">
      <path d="M0,8 H22 V26 H0 L7,17Z" fill="var(--ink)"/>
      <path d="M172,8 H150 V26 H172 L165,17Z" fill="var(--ink)"/>
      <path d="M16,2 Q86,-2 156,2 V22 Q86,18 16,22Z" fill="var(--ink)"/>
    </svg>
    <div class="ribbon-text"><span class="region">STONEBRIDGE VALLEY</span><span class="subregion">HIGH PLAINS</span></div>
    <div class="varietal">
      <span class="small">Single Vineyard</span>
      <span class="grape">Grenache</span>
      <span class="small">Estate Grown Wine</span>
    </div>
    <div class="vintage"><span class="rule"></span><span class="year">2018</span><span class="rule"></span></div>
  </article>

  <p class="spec spec--size">Size: 80mmx100mm</p>
  <p class="spec spec--color">Color</p>
  <div class="palette" aria-label="Print colours: cream, black, brown">
    <span class="chip chip--cream"></span>
    <span class="chip chip--black"></span>
    <span class="chip chip--brown"></span>
  </div>
</main>
</body>
</html>
```